Physiotherapiepraxis braucht Druckvorlage für Werbeanzeige
Zielgruppe
Dienstleistung im Gesundheitswesen als Physiotherapiepraxis.
Krankengymnastik, auch im häuslichen Bereich oder im Altersheim, und Massage sowie Wellnessanwendungen.
Zielgruppe sind primär Erwachsene, eingeschränkt auch Kinder.
Aufgabenstellung
Ich möchte eine Druckvorlage für eine Werbeanzeige, die ich immer mal wieder in verschiedenen Festschriften im dörflichen Bereich oder in einer regionalen Zeitschrift veröffentlichen kann.
Die Anzeige soll das Logo enthalten und die Anschrift der Praxis sowie die Telefonnummer und Adresse der Homepage.

```html
<!DOCTYPE html>
<html lang="de">
<head>
<meta charset="utf-8">
<title>Marlene Hoffgart Physiotherapie – Anzeige</title>
<link rel="stylesheet" href="https://fonts.googleapis.com/css2?family=Open+Sans:wght@400;700&family=Caveat:wght@400&display=swap">
<style>
  :root {
    --page-bg: #ecebe8;
    --ad-bg: #ffffff;
    --ad-border: #2a2a2c;
    --brand-green: #1a7a3a;
    --brand-gold: #d4b52a;
    --panel-dark: #2b2b2d;
    --text-light: #ffffff;
  }
  * { margin: 0; padding: 0; box-sizing: border-box; }
  html, body {
    width: 1200px;
    height: 775px;
    overflow: hidden;
    background: var(--page-bg);
  }
  .canvas {
    position: relative;
    width: 1200px;
    height: 775px;
  }
  .ad {
    position: absolute;
    left: 240px;
    top: 30px;
    width: 720px;
    height: 716px;
    background: var(--ad-bg);
    border: 3px solid var(--ad-border);
    font-family: "Open Sans", Arial, sans-serif;
  }
  .brand {
    position: absolute;
    left: 0;
    right: 0;
    top: 88px;
    display: flex;
    align-items: center;
    justify-content: center;
    gap: 18px;
  }
  .brand-dot {
    width: 26px;
    height: 26px;
    border-radius: 50%;
    background: var(--brand-gold);
  }
  .brand-name {
    color: var(--brand-green);
    font-size: 48px;
    font-weight: 400;
    letter-spacing: 4px;
  }
  .service-band {
    position: absolute;
    left: 42px;
    right: 42px;
    top: 192px;
    height: 90px;
    background: var(--brand-gold);
    color: var(--text-light);
    font-weight: 700;
    font-size: 52px;
    line-height: 90px;
    text-align: center;
    letter-spacing: 1px;
  }
  .info-panel {
    position: absolute;
    left: 42px;
    right: 42px;
    top: 305px;
    height: 368px;
    background: var(--panel-dark);
    color: var(--text-light);
    padding: 26px 26px 0 30px;
  }
  .tagline {
    font-family: "Caveat", cursive;
    font-size: 66px;
    line-height: 64px;
    margin-bottom: 22px;
  }
  .tagline-line2 { padding-left: 96px; display: block; }
  .tagline-accent { color: var(--brand-gold); }
  .contact-list { list-style: none; }
  .contact-item {
    display: flex;
    align-items: center;
    gap: 10px;
    font-size: 33px;
    line-height: 48px;
  }
  .contact-icon {
    width: 26px;
    height: 26px;
    flex: none;
    fill: var(--brand-gold);
  }
</style>
</head>
<body>
<div class="canvas">
  <section class="ad">
    <div class="brand">
      <span class="brand-dot"></span>
      <span class="brand-name">Marlene Hoffgart</span>
    </div>

    <div class="service-band">PHYSIOTHERAPIE</div>

    <div class="info-panel">
      <p class="tagline">Wir bringen Sie<span class="tagline-line2"><span class="tagline-accent">gerne</span> in Bewegung</span></p>
      <ul class="contact-list">
        <li class="contact-item">
          <svg class="contact-icon" viewBox="0 0 24 24" aria-hidden="true"><path d="M12 1a8 8 0 0 0-8 8c0 6 8 14 8 14s8-8 8-14a8 8 0 0 0-8-8zm0 11a3 3 0 1 1 0-6 3 3 0 0 1 0 6z"/></svg>
          Lindenweg 7 in 21499 Hollmoor
        </li>
        <li class="contact-item">
          <svg class="contact-icon" viewBox="0 0 24 24" aria-hidden="true"><path d="M6.6 10.8a15 15 0 0 0 6.6 6.6l2.2-2.2a1 1 0 0 1 1-.25 11.4 11.4 0 0 0 3.6.57 1 1 0 0 1 1 1V20a1 1 0 0 1-1 1A17 17 0 0 1 3 4a1 1 0 0 1 1-1h3.5a1 1 0 0 1 1 1c0 1.25.2 2.45.57 3.6a1 1 0 0 1-.25 1z"/></svg>
          +49 (0)4157 - 24 86 10
        </li>
        <li class="contact-item">
          <svg class="contact-icon" viewBox="0 0 24 24" aria-hidden="true"><path d="M12 2a10 10 0 1 0 0 20 10 10 0 0 0 0-20zm6.9 6h-3a15 15 0 0 0-1.3-3.9A8 8 0 0 1 18.9 8zM12 4c.9 1.2 1.6 2.6 2 4h-4c.4-1.4 1.1-2.8 2-4zM4.3 14a8 8 0 0 1 0-4h3.4a16 16 0 0 0 0 4zm.8 2h3a15 15 0 0 0 1.3 3.9A8 8 0 0 1 5.1 16zm3-8h-3a8 8 0 0 1 4.3-3.9A15 15 0 0 0 8.1 8zM12 20c-.9-1.2-1.6-2.6-2-4h4c-.4 1.4-1.1 2.8-2 4zm2.3-6H9.7a14 14 0 0 1 0-4h4.6a14 14 0 0 1 0 4zm.3 5.9A15 15 0 0 0 15.9 16h3a8 8 0 0 1-4.3 3.9zm1.7-5.9a16 16 0 0 0 0-4h3.4a8 8 0 0 1 0 4z"/></svg>
          www.physiotherapie-hollmoor.de
        </li>
      </ul>
    </div>
  </section>
</div>
</body>
</html>
```